Create look and feel for existing Web Page

Update Web Page

We have a website at http://www.usekivra.com/index-web.html. It is a single page html site, with a custom signup form. We also have a quill bay plugin at the bottom of the page. We'd like to redesign the look and feel of the entire site. We sell software to eye doctors. Also called optometrists, our software tool makes it easy for doctors to manage patients, bill, and document patient encounters. I have included our logos below.

We are looking for a new design preferably in HTML 5, CSS etc. The fields on the form on this page: http://www.usekivra.com/index-web.html

You can get screen shots of our software application at this site: http://staging.usekivra.com
username: test@samplevora.com
password: password

```html
<!DOCTYPE html>
<html lang="en">
<head>
<meta charset="utf-8">
<title>Lumora — Optometry Office Operating System</title>
<link rel="stylesheet" href="https://fonts.googleapis.com/css2?family=Poppins:wght@400;500;600;700&display=swap">
<style>
:root{
  --orange:#f26f21;
  --orange-light:#f7a26c;
  --peach:#fde9dc;
  --dark:#3a3d48;
  --ink:#2f3038;
  --text:#5d5f66;
  --muted:#8a8c93;
  --blue:#4fb3e8;
  --blue-soft:#dff1fb;
  --green:#7cc142;
  --green-soft:#e7f4dc;
  --bg-soft:#f6f6f8;
  --white:#ffffff;
}
*{box-sizing:border-box;margin:0;padding:0}
html,body{width:1200px;height:4494px;overflow:hidden}
body{position:relative;font-family:"Poppins",sans-serif;color:var(--text);background:var(--white)}
.abs{position:absolute}
.btn{position:absolute;display:flex;align-items:center;justify-content:center;border-radius:30px;font-weight:600;font-size:13px;letter-spacing:.5px;text-transform:uppercase;text-decoration:none}
.btn-white{background:var(--white);color:var(--ink);box-shadow:0 6px 16px rgba(0,0,0,.15)}
.btn-orange{background:var(--orange);color:var(--white);box-shadow:0 6px 16px rgba(242,111,33,.3)}
.eyebrow{font-size:14px;font-weight:600;color:var(--orange);text-transform:uppercase;letter-spacing:.5px}
.section-title{font-size:32px;font-weight:600;color:var(--ink);text-align:center;width:1200px;left:0}
.center{text-align:center;width:1200px;left:0}

/* hero */
.brand{font-size:52px;font-weight:500;color:var(--white);left:87px;top:22px;letter-spacing:1px}
.nav a{position:absolute;top:46px;font-size:14px;font-weight:600;color:var(--white);text-decoration:none}
.hero-eyebrow{left:87px;top:207px;font-size:16px;font-weight:600;color:var(--white)}
.hero-title{left:87px;top:228px;font-size:45px;line-height:44px;font-weight:700;color:var(--white)}
.hero-text{left:87px;top:334px;width:480px;font-size:13.5px;line-height:17px;color:var(--white)}
.device{left:636px;top:119px;width:580px;height:456px;border-radius:18px 0 0 18px;background:linear-gradient(160deg,#e9eaec,#c9cbcf)}

/* features */
.feature-card{left:89px;top:1052px;width:1022px;height:493px;background:var(--white);border-radius:8px;box-shadow:0 10px 40px rgba(0,0,0,.07)}
.feature{position:absolute;width:240px}
.feature .icon{width:58px;height:60px;border-radius:10px}
.feature h3{margin-top:16px;font-size:20px;font-weight:600;color:var(--ink)}
.feature p{margin-top:4px;font-size:13.5px;line-height:19px;color:var(--text)}

/* os */
.os-band{left:0;top:1800px;width:1200px;height:590px;background:linear-gradient(180deg,#fff 0%,var(--bg-soft) 30%,var(--bg-soft) 100%)}
.screen{left:89px;top:1896px;width:549px;height:380px;border-radius:10px;background:linear-gradient(90deg,#34363f 0 26%,#f1f2f4 26% 100%);box-shadow:0 10px 30px rgba(0,0,0,.12)}
.os-title{left:741px;top:1935px;font-size:38px;font-weight:600;color:var(--ink)}
.os-text{left:743px;width:370px;font-size:13.5px;line-height:22px;color:var(--text)}

/* pricing */
.price-card{position:absolute;background:var(--white);border-radius:8px;text-align:center;box-shadow:0 10px 30px rgba(0,0,0,.06)}
.price-card h4{font-size:21px;font-weight:500;color:var(--ink)}
.price-card .amount{margin-top:4px;font-size:20px;color:var(--text)}
.price-card .amount b{font-size:62px;font-weight:600}
.price-card .amount small{font-size:20px}
.price-card .per{font-size:18px;color:var(--muted);margin-top:-4px}
.price-card .desc{font-size:14px;line-height:22px;margin:14px 18px 0}
.price-card .btn{position:static;display:inline-flex;margin-top:26px;width:146px;height:40px}
.featured{background:var(--orange);color:var(--white)}
.featured h4,.featured .amount,.featured .per,.featured .desc{color:var(--white)}
.dot{position:absolute;top:2964px;width:9px;height:9px;border-radius:50%;border:1.5px solid #999}

/* waitlist */
.photo{left:70px;top:3322px;width:506px;height:646px;background:linear-gradient(180deg,#e9eef6,#c8d5ea)}
.form-card{left:644px;top:3315px;width:467px;height:522px;background:var(--white);border-radius:8px;box-shadow:0 10px 40px rgba(0,0,0,.08)}
.field{position:absolute;left:35px;width:395px;border-bottom:1.5px solid #cfd1d6;padding-bottom:12px;font-size:13.5px;font-weight:500;color:var(--ink)}
.cta-band{left:0;top:3968px;width:1108px;height:157px;background:var(--dark);border-radius:0 0 90px 0}
.cta-band h2{position:absolute;left:87px;top:52px;font-size:36px;font-weight:600;color:var(--white)}

/* footer */
.foot-brand{left:87px;top:4196px;font-size:90px;font-weight:500;color:#6d6f76;letter-spacing:2px}
.social{position:absolute;top:4323px;width:28px;height:28px;border-radius:50%;background:var(--orange)}
.foot-col h5{font-size:17px;font-weight:600;color:var(--ink);margin-bottom:14px}
.foot-col li{list-style:none;font-size:13.5px;line-height:31.5px;color:var(--text)}
.contact-item{position:absolute;left:895px;display:flex;gap:14px;font-size:13.5px;color:var(--text)}
.contact-item b{display:block;font-size:18px;font-weight:400;color:var(--ink)}
.copyright{top:4458px;font-size:12.5px;font-weight:500;color:var(--text)}
.to-top{left:1134px;top:4411px;width:40px;height:40px;border-radius:50%;background:var(--orange)}
</style>
</head>
<body>

<!-- Hero -->
<header>
  <svg class="abs" style="left:0;top:0" width="1200" height="700" viewBox="0 0 1200 700">
    <path d="M0 0H1120L1200 60V220C1080 420 860 560 640 540C420 520 300 640 180 470C120 400 60 440 0 470Z" fill="var(--orange)"/>
    <path d="M1120 0H1200V150Z" fill="#d7d8db"/>
    <path d="M1140 0H1200V80C1180 60 1160 30 1140 0Z" fill="#5b5d66"/>
    <circle cx="531" cy="572" r="51" fill="#f79a5e" opacity=".8"/>
  </svg>
  <div class="abs brand">lumora</div>
  <nav class="nav">
    <a style="left:623px" href="#">HOME</a>
    <a style="left:712px" href="#">PRODUCTS</a>
    <a style="left:841px" href="#">PRICING</a>
  </nav>
  <a class="btn btn-white" style="left:938px;top:35px;width:105px;height:42px" href="#">Sign up</a>

  <div class="abs hero-eyebrow">LEASE PRACTICES</div>
  <h1 class="abs hero-title">Choose how You<br>spend your time</h1>
  <p class="abs hero-text">Lumora is your office operating system. Automate your painful tasks, keep track of your books, and live a little. Start with a FREE charting tool and add more products as you grow.</p>
  <a class="btn btn-white" style="left:89px;top:412px;width:296px;height:50px" href="#">Get the charting tool for free</a>
  <div class="abs device" role="img" aria-label="Laptop showing the patient charting screen"></div>
</header>

<!-- Features -->
<section>
  <svg class="abs" style="left:0;top:940px" width="1200" height="650" viewBox="0 0 1200 650">
    <path d="M560 80C680 -20 880 -10 1000 60C1080 100 1150 60 1200 40V650H700C900 520 760 300 560 80Z" fill="var(--peach)" opacity=".7"/>
  </svg>
  <div class="abs eyebrow center" style="top:801px">Join the cool club</div>
  <h2 class="abs section-title" style="top:820px">AI to Automate Optometry Office Tasks</h2>
  <p class="abs center" style="top:893px;font-size:14px">Lumora uses AI, automation, robots, and other cool technology to streamline office work so you can do things you love</p>

  <div class="abs feature-card">
    <div class="feature" style="left:51px;top:47px"><div class="icon" style="background:#f7c9c6"></div><h3>Schedule</h3><p>Meet your patients where they are, 24 hours 7 days a week with the online scheduler.</p></div>
    <div class="feature" style="left:387px;top:47px"><div class="icon" style="background:#bfe3f6"></div><h3>Intake</h3><p>Never print out another paper form. Your patients are now able to fill out &amp; sign forms online.</p></div>
    <div class="feature" style="left:725px;top:47px"><div class="icon" style="background:#fcd7bd"></div><h3>Chart</h3><p>Start charting all patient findings for FREE. With features like auto population it flies on your mobile phone.</p></div>
    <div class="feature" style="left:51px;top:265px"><div class="icon" style="background:#fde6a8"></div><h3>Bill</h3><p>Don't waste your precious time or pay someone to bill insurance, let a bot do it for you.</p></div>
    <div class="feature" style="left:387px;top:265px"><div class="icon" style="background:#dccff6"></div><h3>Eligible</h3><p>Don't call or login into every insurance website to get patient eligibility &amp; copays. Our bots do that too.</p></div>
    <div class="feature" style="left:725px;top:265px"><div class="icon" style="background:#d5ecc2"></div><h3>Review</h3><p>Grow your patient base and improve your search results with the review solution.</p></div>
  </div>
</section>

<!-- Practice OS -->
<section>
  <div class="abs os-band"></div>
  <h2 class="abs section-title" style="top:1742px">Practice Operating System</h2>
  <div class="abs" style="left:566px;top:1794px;width:68px;height:3px;background:#d5d6da"></div>
  <div class="abs screen" role="img" aria-label="Dashboard screen with sales and revenue panels"></div>
  <svg class="abs" style="left:32px;top:2082px" width="26" height="52" viewBox="0 0 26 52" fill="none" stroke="var(--ink)" stroke-width="1.8">
    <path d="M2 11H22M15 4L22 11L15 18"/><path d="M24 40H4M11 33L4 40L11 47"/>
  </svg>
  <h3 class="abs os-title">Dashboard</h3>
  <p class="abs os-text" style="top:2014px">Aenean lorem quis bibendum auctor sed odio sit amet nibh vulputate cursus a sit amet maurisipsum velit. Nam nec tellus a odio tincidunt auctor a ornare odio. Sed non mauris vitae erat</p>
  <p class="abs os-text" style="top:2125px">consequat auctor eu in elit. Class aptent taciti sociosqu ad litora torquent per conubia nostra...</p>
  <a class="btn btn-orange" style="left:743px;top:2192px;width:145px;height:42px" href="#">Learn more</a>
</section>

<!-- Pricing -->
<section>
  <div class="abs" style="left:0;top:2389px;width:1200px;height:733px;background:var(--bg-soft)"></div>
  <h2 class="abs section-title" style="top:2460px">Our Pricing Plan</h2>

  <div class="price-card" style="left:89px;top:2574px;width:328px;height:321px;padding-top:26px;border-bottom:3px solid var(--blue)">
    <h4>Free</h4>
    <div class="amount">From <b style="color:var(--blue)">$0</b></div>
    <div class="per">No strings attached</div>
    <p class="desc">Chart patient findings for FREE. Unlimited users, doctors, and location.</p>
    <a class="btn" style="background:var(--blue-soft);color:var(--blue)" href="#">Choose plan</a>
  </div>
  <div class="price-card featured" style="left:436px;top:2539px;width:328px;height:394px;padding-top:60px;border-bottom:4px solid #d85c14">
    <h4>Pick 1 Add On</h4>
    <div class="amount">From <b>$99</b><small>/mo</small></div>
    <div class="per">Per Location</div>
    <p class="desc">Choose one feature between schedule, intake, bill, eligible, or review.</p>
    <a class="btn btn-white" href="#">Choose plan</a>
  </div>
  <div class="price-card" style="left:781px;top:2574px;width:330px;height:321px;padding-top:26px;border-bottom:3px solid var(--green)">
    <h4>Pick 2 Add Ons</h4>
    <div class="amount">From <b style="color:var(--green)">$99</b><small>/mo</small></div>
    <div class="per">Per Location</div>
    <p class="desc">Choose any two features between schedule, intake, bill, eligible, &amp;/or review.</p>
    <a class="btn" style="background:var(--green-soft);color:var(--green)" href="#">Choose plan</a>
  </div>
  <span class="dot" style="left:578px;border-color:#333"></span>
  <span class="dot" style="left:596px"></span>
  <span class="dot" style="left:614px"></span>
</section>

<!-- Waitlist -->
<section>
  <div class="abs eyebrow center" style="top:3163px">Get on the waitlist</div>
  <h2 class="abs section-title" style="top:3183px">Get Started With A Free Charting Tool</h2>
  <p class="abs center" style="top:3247px;font-size:14px">Become part of a club that wants to change the way we practice, so we can have a life outside of the office.</p>
  <div class="abs photo" role="img" aria-label="Photo of a smiling man in glasses pointing toward the signup form"></div>
  <form class="abs form-card">
    <label class="field" style="top:42px">Full Name*</label>
    <label class="field" style="top:120px">Email*</label>
    <label class="field" style="top:199px">Phone Number*</label>
    <label class="field" style="top:279px">Office Name*</label>
    <label class="field" style="top:358px">NPI*</label>
    <a class="btn btn-orange" style="left:85px;top:428px;width:296px;height:47px" href="#">Get the charting tool for free</a>
  </form>
  <div class="abs cta-band">
    <h2>Now spend time outside the office!</h2>
    <a class="btn btn-white" style="left:889px;top:50px;width:154px;height:46px" href="#">Join the club</a>
  </div>
</section>

<!-- Footer -->
<footer>
  <div class="abs foot-brand">lumora</div>
  <span class="social" style="left:139px"></span>
  <span class="social" style="left:180px"></span>
  <span class="social" style="left:220px"></span>
  <span class="social" style="left:262px"></span>

  <div class="abs foot-col" style="left:450px;top:4193px">
    <h5>Quick Links</h5>
    <ul><li>› Home</li><li>› Product</li><li>› Pricing Plan</li><li>› Sign Up</li></ul>
  </div>
  <div class="abs foot-col" style="left:675px;top:4193px">
    <h5>Information</h5>
    <ul><li>› Blog</li><li>› About Us</li><li>› Partners</li><li>› Resources</li><li>› Contact</li></ul>
  </div>
  <div class="abs foot-col" style="left:895px;top:4193px"><h5>Contact info</h5></div>
  <div class="contact-item" style="top:4244px">
    <svg width="24" height="24" viewBox="0 0 24 24" style="margin-top:10px"><rect x="1" y="4" width="22" height="16" rx="2" fill="var(--orange)"/><path d="M2 6L12 13L22 6" stroke="#fff" stroke-width="1.8" fill="none"/></svg>
    <div>Email:<b>info@lumora.com</b></div>
  </div>
  <div class="contact-item" style="top:4316px">
    <svg width="24" height="24" viewBox="0 0 24 24" style="margin-top:10px"><path d="M5 2L9 2L11 7L8.5 9C9.6 11.5 12.5 14.4 15 15.5L17 13L22 15V19C22 20.5 20.5 22 19 22C9.6 21.4 2.6 14.4 2 5C2 3.5 3.5 2 5 2Z" fill="var(--orange)"/></svg>
    <div>Phone:<b>+08 123-555-0190</b></div>
  </div>
  <a class="abs to-top" href="#" aria-label="Back to top">
    <svg width="40" height="40" viewBox="0 0 40 40"><path d="M20 27V13M14 19L20 13L26 19" stroke="#fff" stroke-width="2" fill="none"/></svg>
  </a>
  <div class="abs center copyright">© 2020 LUMORA, ALL RIGHTS RESERVED.</div>
</footer>

</body>
</html>
```